Gutschein-Design für Baumhaus-Vermietung
Zielgruppe
Das Leben in einem Baumhaus verspricht Entspannung, Abenteuer, Entdeckungen, Spaß, Spiel und Naturbeobachtungen. Unsere gemütlichen Baumhäuser bieten Ihnen einen naturverbundenen Urlaub mit vielen aufregenden Erlebnissen.
Aufgabenstellung
Das Logo soll unbedingt verwendet werden. Das Format sollte DIN a4 sein, dass wir es über unseren Drucker erstellen können. Als Angaben auf dem Gutschein zur Identifikation wird eine Gutscheinnummer und ein Ausstellungsdatum benötigt. Dazu unsere Adresse und die Kontaktdaten. Es handelt sich um einen Wertgutschein (der dann als Urlaubscheck eingelöst werden kann)

```html
<!DOCTYPE html>
<html lang="de">
<head>
<meta charset="utf-8">
<title>Gutschein – Ferienhof Waldkrone</title>
<link href="https://fonts.googleapis.com/css2?family=Jost:wght@400;500;700&family=Dancing+Script:wght@600;700&display=swap" rel="stylesheet">
<style>
  :root {
    --forest: #1e6b3a;
    --forest-deep: #175a30;
    --bark: #8a6a45;
    --rule: #b49a78;
    --paper: #ffffff;
    --stage: #ecebe7;
    --white: #ffffff;
  }
  * { box-sizing: border-box; margin: 0; padding: 0; }
  html, body { width: 1200px; height: 841px; overflow: hidden; }
  body { background: var(--stage); font-family: "Jost", sans-serif; }

  .voucher {
    position: absolute; left: 320px; top: 24px;
    width: 560px; height: 792px;
    background: var(--paper);
    box-shadow: 0 4px 18px rgba(0,0,0,.12);
    overflow: hidden;
  }
  .leaf-pattern {
    position: absolute; left: 0; top: 0; width: 100%; height: 420px;
    background:
      radial-gradient(ellipse at 85% 12%, rgba(190,215,170,.35), transparent 45%),
      radial-gradient(ellipse at 8% 55%, rgba(190,215,200,.35), transparent 40%);
  }
  .brand {
    position: absolute; top: 52px; left: 0; width: 100%;
    display: flex; justify-content: center; align-items: center; gap: 12px;
  }
  .brand-dot { width: 46px; height: 46px; border-radius: 50%; background: var(--bark); }
  .brand-name { font-weight: 700; font-size: 30px; color: var(--forest); letter-spacing: .5px; }

  .title {
    position: absolute; top: 150px; width: 100%; text-align: center;
    font-family: "Dancing Script", cursive; font-weight: 700;
    font-size: 64px; color: var(--forest);
  }
  .label {
    position: absolute; width: 100%; text-align: center;
    font-size: 14px; color: var(--bark); letter-spacing: .5px;
  }
  .label-value { top: 238px; }
  .label-for { top: 322px; }
  .field-line { position: absolute; height: 1px; background: var(--rule); }
  .line-value { left: 110px; width: 340px; top: 296px; }
  .line-for-1 { left: 110px; width: 340px; top: 378px; }
  .line-for-2 { left: 110px; width: 340px; top: 430px; }

  .voucher-number {
    position: absolute; left: 70px; top: 472px;
    display: flex; align-items: flex-end; gap: 6px;
    font-size: 11px; color: var(--bark);
  }
  .voucher-number span.line { display: block; width: 140px; height: 1px; background: var(--rule); margin-bottom: 3px; }

  .gallery { position: absolute; left: 0; top: 512px; width: 100%; height: 130px; display: flex; }
  .photo { flex: 1; }
  .photo-garden { background: linear-gradient(160deg, #6d9a5a, #2f5a2c 60%, #8a6a45); }
  .photo-bedroom { background: linear-gradient(160deg, #c99a68, #e9dccb 55%, #a8774b); }
  .photo-bath { background: linear-gradient(160deg, #b98b5f, #6a5342 55%, #c9a37a); }

  .contact-band {
    position: absolute; left: 0; top: 642px; width: 100%; height: 150px;
    background: var(--forest); color: var(--white);
    display: flex; justify-content: space-between; padding: 26px 36px 0 36px;
  }
  .address { display: flex; gap: 14px; }
  .address-name { font-family: "Dancing Script", cursive; font-weight: 600; font-size: 21px; margin-bottom: 4px; }
  .address p { font-size: 15px; line-height: 1.35; }
  .contacts { list-style: none; }
  .contacts li { display: flex; align-items: center; gap: 12px; font-size: 14px; margin-bottom: 12px; }
  .contacts li.web { font-weight: 700; }
  .icon { width: 22px; height: 22px; flex: none; fill: none; stroke: var(--white); stroke-width: 1.4; stroke-linecap: round; stroke-linejoin: round; }
</style>
</head>
<body>
  <article class="voucher">
    <div class="leaf-pattern" role="img" aria-label="Zartes Muster aus hellen Blättern"></div>

    <header class="brand">
      <span class="brand-dot"></span>
      <span class="brand-name">Ferienhof Waldkrone</span>
    </header>

    <h1 class="title">Gutschein</h1>
    <div class="label label-value">im Wert von</div>
    <div class="field-line line-value"></div>
    <div class="label label-for">für</div>
    <div class="field-line line-for-1"></div>
    <div class="field-line line-for-2"></div>

    <div class="voucher-number">Gutschein-Nr. <span class="line"></span></div>

    <section class="gallery">
      <div class="photo photo-garden" role="img" aria-label="Foto: Baumhaus mit Holzterrasse zwischen Bäumen"></div>
      <div class="photo photo-bedroom" role="img" aria-label="Foto: Schlafzimmer im Baumhaus mit Holzwänden"></div>
      <div class="photo photo-bath" role="img" aria-label="Foto: Badezimmer mit Holzverkleidung und Steinwaschbecken"></div>
    </section>

    <footer class="contact-band">
      <div class="address">
        <svg class="icon" viewBox="0 0 24 24"><path d="M12 14s5-5 5-8.5a5 5 0 0 0-10 0C7 9 12 14 12 14z"/><circle cx="12" cy="5.5" r="1.8"/><path d="M6 14l-4 7h20l-4-7"/></svg>
        <div>
          <div class="address-name">Ferienhof Waldkrone</div>
          <p>Familie Lindqvist<br>Birkenweg 12<br>87400 Tannried</p>
        </div>
      </div>
      <ul class="contacts">
        <li><svg class="icon" viewBox="0 0 24 24"><path d="M5 3h4l2 5-2.5 1.5a11 11 0 0 0 6 6L16 13l5 2v4a2 2 0 0 1-2 2A17 17 0 0 1 3 5a2 2 0 0 1 2-2z"/></svg>+ 49 (0) 1234 567890</li>
        <li><svg class="icon" viewBox="0 0 24 24"><rect x="2" y="5" width="20" height="14" rx="1"/><path d="M2 6l10 7 10-7"/></svg>info@waldkrone-ferien.de</li>
        <li class="web"><svg class="icon" viewBox="0 0 24 24"><circle cx="12" cy="12" r="10"/><path d="M2 12h20M12 2c3 3 3 17 0 20M12 2c-3 3-3 17 0 20M4 7h16M4 17h16"/></svg>www.waldkrone-ferien.de</li>
      </ul>
    </footer>
  </article>
</body>
</html>
```